Business card & stationery for audio visual & security system installation company
Audio visual & security system installations
I need double sided standard sized Business Card [3.5" x 2"]
Up to the designer
Professional
Teodor Malsk
Suite 418, 6 -10 Quenby Street,
Marrowby Heights, 2999
teodor@plenvo.com.au
www.plenvo.com.au
Master Cabler No - K519207
Logo on the front
Logo on the back

```html
<!DOCTYPE html>
<html lang="en">
<head>
<meta charset="utf-8">
<title>Plenvo Stationery Set</title>
<link href="https://fonts.googleapis.com/css2?family=Open+Sans:wght@400;600;700&display=swap" rel="stylesheet">
<style>
  :root{
    --bg:#e4e4e4;
    --paper:#ffffff;
    --red:#d3202a;
    --red-soft:rgba(211,32,42,.09);
    --charcoal:#3a3a3c;
    --charcoal-dark:#2a2a2c;
    --band-dark:#1f1f21;
    --band-mid:#5c5c5e;
    --band-light:#d2d2d2;
    --line:#9a9a9a;
    --ink:#333;
    --white:#fff;
  }
  *{box-sizing:border-box;margin:0;padding:0}
  html,body{width:1200px;height:886px;overflow:hidden}
  body{background:var(--bg);font-family:"Open Sans",Arial,sans-serif;color:var(--ink);position:relative}

  .sheet{position:absolute;background:var(--paper);box-shadow:0 2px 8px rgba(0,0,0,.18);overflow:hidden}
  .band{position:absolute;left:0;right:0;background:linear-gradient(90deg,var(--band-dark),var(--band-mid) 55%,var(--band-light))}

  .brand{display:flex;align-items:center;gap:6px;color:var(--red);font-weight:700;letter-spacing:.5px;white-space:nowrap}
  .brand-dot{display:inline-block;border-radius:50%;background:var(--red)}

  .services{position:absolute;color:var(--red);font-size:6px;line-height:9px;text-align:left;white-space:nowrap}
  .services span{display:block}

  .watermark{position:absolute;display:flex;align-items:center;justify-content:center;gap:14px;color:var(--red-soft);font-weight:700}
  .watermark .wm-dot{border-radius:50%;background:var(--red-soft)}

  /* letterhead */
  .letterhead{left:32px;top:32px;width:396px;height:560px}
  .letterhead .band{top:34px;height:40px}
  .letterhead .brand{position:absolute;right:70px;top:42px;font-size:22px}
  .letterhead .brand-dot{width:12px;height:12px}
  .letterhead .services{right:12px;top:80px}
  .letterhead .watermark{left:0;right:0;top:300px;font-size:64px}
  .letterhead .wm-dot{width:60px;height:60px}

  /* fax */
  .fax{left:452px;top:32px;width:396px;height:560px}
  .fax .band{top:0;height:56px;background:linear-gradient(90deg,var(--band-dark),var(--band-mid) 60%,var(--band-light))}
  .fax .brand{position:absolute;left:90px;top:12px;font-size:24px}
  .fax .brand-dot{width:13px;height:13px}
  .fax .services{right:12px;top:60px}
  .fax-table{position:absolute;left:20px;top:78px;width:300px;border-collapse:collapse;font-size:8px}
  .fax-table td{border:1px solid var(--line);height:20px;padding:2px 5px;vertical-align:top}
  .fax-table .label{width:40px}
  .fax-title{position:absolute;right:22px;top:156px;font-size:14px;font-weight:700;color:var(--ink)}
  .fax-rule{position:absolute;left:20px;right:20px;top:178px;border-top:2px solid var(--ink)}
  .fax-checks{position:absolute;left:20px;right:20px;top:186px;display:flex;justify-content:space-between;font-size:7px}
  .fax-checks span{display:flex;align-items:center;gap:3px}
  .fax-checks i{display:inline-block;width:7px;height:7px;border:1px solid var(--ink)}
  .fax .watermark{left:0;right:0;top:320px;font-size:64px}
  .fax .wm-dot{width:60px;height:60px}

  /* envelope */
  .envelope{left:872px;top:32px;width:296px;height:148px}
  .envelope .flap{position:absolute;left:0;top:0}
  .envelope .brand{position:absolute;left:112px;top:14px;font-size:16px}
  .envelope .brand-dot{width:9px;height:9px}
  .envelope .band{top:58px;height:14px}
  .envelope .return{position:absolute;left:12px;top:78px;font-size:5.5px;color:var(--ink);white-space:nowrap}

  /* compliments slip */
  .slip{left:872px;top:204px;width:296px;height:120px}
  .slip .band{top:12px;height:26px}
  .slip .brand{position:absolute;right:50px;top:15px;font-size:15px}
  .slip .brand-dot{width:8px;height:8px}
  .slip .services{right:8px;top:42px;font-size:5px;line-height:7px}
  .slip .greeting{position:absolute;left:14px;top:48px;font-size:8px;color:var(--ink)}
  .slip .watermark{left:0;right:0;top:76px;font-size:30px}
  .slip .wm-dot{width:28px;height:28px}

  /* business cards */
  .card{position:absolute;width:266px;height:152px;border-radius:10px;background:var(--charcoal);overflow:hidden;box-shadow:0 2px 8px rgba(0,0,0,.25)}
  .card .band{top:0;height:30px;background:linear-gradient(90deg,var(--band-dark),var(--band-mid) 60%,#9d9d9f)}
  .card-front .brand{position:absolute;right:16px;top:34px;font-size:18px}
  .card-front .brand-dot{width:10px;height:10px}
  .card-name{position:absolute;left:16px;top:64px;color:var(--red);font-size:11px;font-weight:700}
  .card-role{position:absolute;left:16px;top:79px;color:var(--white);font-size:7px}
  .card-contact{position:absolute;right:14px;top:68px;color:var(--white);font-size:6.5px;line-height:10px;text-align:left;white-space:nowrap}
  .card-contact span{display:flex;align-items:center;gap:4px}
  .card-contact .indent{padding-left:10px}
  .card-contact svg{flex:none}
  .card-back{background:var(--charcoal-dark)}
  .card-back .brand{position:absolute;left:0;right:0;top:52px;justify-content:center;font-size:24px}
  .card-back .brand-dot{width:13px;height:13px}
  .card-web{position:absolute;left:0;right:0;bottom:22px;text-align:center;color:var(--white);font-size:8px;letter-spacing:1px}
  .card-web b{color:var(--red);font-weight:600}

  .pos-1{left:32px;top:626px}
  .pos-2{left:322px;top:626px}
  .pos-3{left:612px;top:626px}
  .pos-4{left:902px;top:626px}
</style>
</head>
<body>

  <!-- Letterhead -->
  <section class="sheet letterhead" aria-label="Letterhead">
    <div class="band"></div>
    <div class="brand"><span class="brand-dot"></span>Plenvo</div>
    <div class="services">
      <span>Audio Visual Installs</span>
      <span>Security Systems</span>
      <span>Home Theatre</span>
      <span>Data &amp; Cabling</span>
    </div>
    <div class="watermark"><span class="wm-dot"></span>Plenvo</div>
  </section>

  <!-- Fax sheet -->
  <section class="sheet fax" aria-label="Fax cover sheet">
    <div class="band"></div>
    <div class="brand"><span class="brand-dot"></span>Plenvo</div>
    <div class="services">
      <span>Audio Visual Installs</span>
      <span>Security Systems</span>
      <span>Home Theatre</span>
      <span>Data &amp; Cabling</span>
    </div>
    <table class="fax-table">
      <tr><td class="label">To:</td><td></td><td class="label">From:</td><td></td></tr>
      <tr><td class="label">Fax:</td><td></td><td class="label">Pages:</td><td></td></tr>
      <tr><td class="label">Phone:</td><td></td><td class="label">Date:</td><td></td></tr>
      <tr><td class="label">Re:</td><td></td><td class="label">CC:</td><td></td></tr>
    </table>
    <div class="fax-title">FAX</div>
    <div class="fax-rule"></div>
    <div class="fax-checks">
      <span><i></i>Urgent</span>
      <span><i></i>For Review</span>
      <span><i></i>Please Comment</span>
      <span><i></i>Please Reply</span>
      <span><i></i>Please Recycle</span>
    </div>
    <div class="watermark"><span class="wm-dot"></span>Plenvo</div>
  </section>

  <!-- DL envelope -->
  <section class="sheet envelope" aria-label="Envelope">
    <svg class="flap" width="296" height="56" viewBox="0 0 296 56" aria-hidden="true">
      <path d="M0 0 L148 52 L296 0" fill="none" stroke="#cfcfcf" stroke-width="1"/>
    </svg>
    <div class="brand"><span class="brand-dot"></span>Plenvo</div>
    <div class="band"></div>
    <div class="return">Suite 418, 6 -10 Quenby Street, Marrowby Heights, 2999</div>
  </section>

  <!-- Compliments slip -->
  <section class="sheet slip" aria-label="Compliments slip">
    <div class="band"></div>
    <div class="brand"><span class="brand-dot"></span>Plenvo</div>
    <div class="services">
      <span>Audio Visual Installs</span>
      <span>Security Systems</span>
    </div>
    <div class="greeting">With Compliments</div>
    <div class="watermark"><span class="wm-dot"></span>Plenvo</div>
  </section>

  <!-- Business card fronts -->
  <article class="card card-front pos-1" aria-label="Business card front">
    <div class="band"></div>
    <div class="brand"><span class="brand-dot"></span>Plenvo</div>
    <div class="card-name">Teodor Malsk</div>
    <div class="card-role">Director</div>
    <div class="card-contact">
      <span><svg width="6" height="7" viewBox="0 0 10 12"><path d="M5 0a4 4 0 0 1 4 4c0 3-4 8-4 8S1 7 1 4a4 4 0 0 1 4-4z" fill="#d3202a"/></svg>Suite 418, 6 -10 Quenby Street,</span>
      <span class="indent">Marrowby Heights, 2999</span>
      <span><svg width="6" height="6" viewBox="0 0 10 10"><path d="M2 0l2 3-1 1c1 2 2 3 3 3l1-1 3 2-1 2C4 10 0 6 0 1z" fill="#d3202a"/></svg>T 01 5550 4172</span>
      <span class="indent">M 0400 555 306</span>
      <span><svg width="6" height="5" viewBox="0 0 10 8"><rect width="10" height="8" fill="#d3202a"/><path d="M0 0l5 4 5-4" stroke="#3a3a3c" fill="none"/></svg>teodor@plenvo.com.au</span>
      <span class="indent">www.plenvo.com.au</span>
      <span class="indent">Master Cabler No - K519207</span>
    </div>
  </article>

  <article class="card card-front pos-2" aria-label="Business card front">
    <div class="band"></div>
    <div class="brand"><span class="brand-dot"></span>Plenvo</div>
    <div class="card-name">Teodor Malsk</div>
    <div class="card-role">Director</div>
    <div class="card-contact">
      <span>Suite 418, 6 -10 Quenby Street,</span>
      <span>Marrowby Heights, 2999</span>
      <span>T 01 5550 4172</span>
      <span>M 0400 555 306</span>
      <span>teodor@plenvo.com.au</span>
      <span>www.plenvo.com.au</span>
      <span>Master Cabler No - K519207</span>
    </div>
  </article>

  <!-- Business card backs -->
  <article class="card card-back pos-3" aria-label="Business card back">
    <div class="brand"><span class="brand-dot"></span>Plenvo</div>
    <div class="card-web">www.<b>plenvo</b>.com.au</div>
  </article>

  <article class="card card-back pos-4" aria-label="Business card back">
    <div class="brand"><span class="brand-dot"></span>Plenvo</div>
    <div class="card-web">www.<b>plenvo</b>.com.au</div>
  </article>

</body>
</html>
```